Sign Design

We already have a logo, but would like to design 2 x signs.
Sign 1:
Dimensions 1500mm wide x 2500m high.
Information to include on sign: - Clinic name and logo (attached)
- the word "DENTIST "
- Street number (which is 348)
Phone number (which is 6153 4097)

Sign 2:
Dimensions: 800mm wide x 600mm high

```html
<!DOCTYPE html>
<html lang="en">
<head>
<meta charset="utf-8">
<title>Kellbrook Dental Care – Signage</title>
<link href="https://fonts.googleapis.com/css2?family=Montserrat:wght@400;500;700;800&family=Noto+Sans:wght@400&display=swap" rel="stylesheet">
<style>
  :root{
    --bg:#6f6f6f;
    --paper:#f7f7f7;
    --forest:#116b35;
    --lime:#a3e04a;
    --mint:#b2e4bc;
    --pale:#e0f2c8;
    --cream:#f1f9e3;
    --ink:#1a1a1a;
    --label:#ffffff;
  }
  *{margin:0;padding:0;box-sizing:border-box}
  html,body{width:1200px;height:857px;overflow:hidden}
  body{background:var(--bg);position:relative;font-family:"Montserrat",sans-serif}
  .size-label{position:absolute;font-family:"Noto Sans",sans-serif;font-size:20px;color:var(--label);letter-spacing:.5px;line-height:1}
  .size-label--tall{left:134px;top:58px}
  .size-label--wide{left:643px;top:179px}
  .sign{position:absolute;background:var(--paper);overflow:hidden;box-shadow:0 6px 18px rgba(0,0,0,.35)}
  .sign--tall{left:99px;top:112px;width:380px;height:633px}
  .sign--wide{left:572px;top:239px;width:507px;height:380px}
  .sign__backdrop{position:absolute;inset:0}
  .sign--tall .sign__backdrop{background:linear-gradient(180deg,var(--paper) 0%,var(--paper) 20%,var(--cream) 32%,var(--pale) 55%,var(--cream) 80%,var(--paper) 100%)}
  .sign--wide .sign__backdrop{background:linear-gradient(160deg,var(--pale) 0%,var(--paper) 25%,var(--paper) 50%,var(--cream) 72%,var(--pale) 100%)}
  .abs{position:absolute;line-height:1;white-space:nowrap}
  .brand-dot{position:absolute;border-radius:50%;background:var(--lime)}
  .brand-name{color:var(--forest);font-weight:400}
  .headline{left:44px;top:224px;font-size:64px;font-weight:800;color:var(--forest);letter-spacing:1px}
  .street{position:absolute;left:47px;top:308px;width:285px;height:81px;display:flex;border:1px solid var(--pale)}
  .street__label{width:181px;background:var(--forest);color:var(--pale);font-weight:800;font-size:31px;line-height:29px;text-align:right;padding:12px 16px 0 0}
  .street__value{flex:1;background:var(--lime);color:var(--forest);font-weight:800;font-size:34px;display:flex;align-items:center;justify-content:center;margin-left:3px}
  .phone-title{left:54px;top:418px;font-size:34px;font-weight:700;color:var(--ink)}
  .phone-pill{position:absolute;left:48px;top:455px;width:285px;height:44px;border-radius:22px;background:var(--forest);border:1px solid var(--pale);display:flex;align-items:center;justify-content:center;gap:10px;color:var(--pale);font-weight:800;font-size:33px}
  .phone-pill svg{width:30px;height:30px}
  .web{color:var(--ink);font-weight:700}
  .web span{color:var(--forest)}
</style>
</head>
<body>
  <div class="size-label size-label--tall">1500mm wide x 2500m high</div>
  <div class="size-label size-label--wide">800mm wide x 600mm high</div>

  <section class="sign sign--tall" aria-label="Tall sign">
    <div class="sign__backdrop" role="img" aria-label="Soft flowing green wave background"></div>
    <div class="brand-dot" style="left:46px;top:66px;width:72px;height:72px"></div>
    <div class="abs brand-name" style="left:141px;top:63px;font-size:44px;letter-spacing:-1.5px">Kellbrook</div>
    <div class="abs brand-name" style="left:210px;top:101px;font-size:25px;letter-spacing:-.5px">Dental Care</div>

    <div class="abs headline">DENTIST</div>

    <div class="street">
      <div class="street__label">Street<br>Number</div>
      <div class="street__value">348</div>
    </div>

    <div class="abs phone-title">Phone Number</div>
    <div class="phone-pill">
      <svg viewBox="0 0 30 30" aria-hidden="true">
        <circle cx="15" cy="15" r="13" fill="none" stroke="currentColor" stroke-width="2"/>
        <path d="M10 8 l3 0 l1.5 4 l-2 1.5 c1 2.2 2.5 3.7 4.5 4.5 l1.5 -2 l4 1.5 l0 3 c-7 1 -13.5 -5.5 -12.5 -12.5 Z" fill="currentColor"/>
      </svg>
      6153 4097
    </div>

    <div class="abs web" style="left:51px;top:548px;font-size:18.5px">Kellbrook<span>DentalCare</span>.com.au</div>
  </section>

  <section class="sign sign--wide" aria-label="Wide sign">
    <div class="sign__backdrop" role="img" aria-label="Soft flowing green wave background"></div>
    <div class="brand-dot" style="left:50px;top:108px;width:104px;height:104px"></div>
    <div class="abs brand-name" style="left:185px;top:106px;font-size:60px;letter-spacing:-2px">Kellbrook</div>
    <div class="abs brand-name" style="left:283px;top:161px;font-size:36px;letter-spacing:-1px">Dental Care</div>
    <div class="abs web" style="left:46px;top:264px;font-size:27.5px">Kellbrook<span>DentalCare</span>.com.au</div>
  </section>
</body>
</html>
```